Zielgruppe
Ich erstelle und vermarkte hochwertige Ebooks/Taschenbücher über Veltrano. Zielgruppe sind Veltrano Lumio Kunden.
Translate to english with google translater:
I create and market high-quality ebooks/paperbacks via Veltrano. The target group are Veltrano Lumio customers.
Aufgabenstellung
Es geht sowohl um die Gestaltung eines Taschenbuch-Covers als auch um die Gestaltung eines Ebook-Covers.
Die Gesamtaufmachung soll schlicht und in sich stimmig sein, ohne viel Schnörkel.
Der Buchtitel lautet wie folgt: Kochbuch für Hobbyköche, Anfänger, Berufstätige und Studenten
Der Untertitel in etwa halber Schriftgröße lautet wie folgt: Mit den 150 besten und originellsten Rezepten für einen perfekten Einstieg
Pseudonym des Autors am unteren Ende: Matthias Wendrauer
Farbliche Aufmachung: Der Hintergrund ein sehr dunkles Rot, Außen ganz dunkel, nach Innen hin zur Mitte etwas heller in fließendem Übergang. Die Schrift in schlichtem Weiß.
Gestalterische Aufmachung: Normale Schriftart. Ausgenommen 'Kochbuch', 'Kochbuch' in Schriftart ähnlich wie Schriftart Monotype Corsiva. Im unterem Bereich Rechts ein Bild eines bunten originellen Gerichts - Nudelgericht - aus der Vogelperspektive, Links einige Gewürze verstreut und einen echten Kochlöffel in dunklem Braun. Genaue Anordnung überlasse ich dem Designer.
It's about designing a paperback cover as well as designing an ebook cover.
The overall presentation should be simple and coherent, without a lot of frills.
The book title is as follows: Kochbuch für Hobbyköche, Anfänger, Berufstätige und Studenten
The subtitle in about half font size is as follows: Mit den 150 besten und originellsten Rezepten für einen perfekten Einstieg
Author's pseudonym at the bottom: Matthias Wendrauer
Color presentation: The background is a very dark red, very dark on the outside, slightly lighter towards the middle in a flowing transition. The font is plain white.
Design: Normal font. Except 'Kochbuch', 'Kochbuch' in font similar to Monotype Corsiva font. In the lower area on the right a picture of a colorful original dish - pasta dish - from a bird's eye view, on the left some spices scattered around and a real wooden spoon in dar..

```html
<!DOCTYPE html>
<html lang="de">
<head>
<meta charset="utf-8">
<title>Kochbuch – Cover</title>
<link rel="stylesheet" href="https://fonts.googleapis.com/css2?family=Cormorant+Garamond:ital,wght@1,500&family=EB+Garamond:ital@1&family=Poppins:wght@300;400&display=swap">
<style>
  :root {
    --bg-deep: #070203;
    --bg-mid: #2a0806;
    --bg-glow: #4a120c;
    --text: #ffffff;
    --text-soft: #e9e3e1;
    --gold: #cdb88e;
    --frame: rgba(255,255,255,0.7);
    --code-box: #615b62;
    --food-warm: rgba(120, 70, 30, 0.55);
    --food-light: rgba(190, 170, 130, 0.35);
  }
  html, body { margin: 0; padding: 0; overflow: hidden; }
  body { width: 1200px; height: 933px; background: var(--bg-deep); }

  .cover-wrap {
    position: relative;
    width: 1200px; height: 933px;
    overflow: hidden;
    background:
      radial-gradient(ellipse 330px 460px at 290px 330px, var(--bg-glow) 0%, var(--bg-mid) 45%, transparent 100%),
      radial-gradient(ellipse 360px 480px at 880px 360px, var(--bg-glow) 0%, var(--bg-mid) 45%, transparent 100%),
      var(--bg-deep);
  }

  .title-script {
    position: absolute;
    margin: 0;
    font-family: "Cormorant Garamond", serif;
    font-style: italic;
    font-weight: 500;
    color: var(--text);
    line-height: 1;
    white-space: nowrap;
  }
  .subtitle-caps {
    position: absolute;
    margin: 0;
    font-family: "Poppins", sans-serif;
    color: var(--text);
    text-transform: uppercase;
    text-align: center;
    white-space: nowrap;
  }

  /* Back cover */
  .back-frame {
    position: absolute;
    left: 48px; top: 104px; width: 498px; height: 520px;
    border: 1px solid var(--frame);
    border-top: none;
  }
  .back-frame::before, .back-frame::after {
    content: ""; position: absolute; top: 0; height: 1px; background: var(--frame);
  }
  .back-frame::before { left: 0; width: 97px; }
  .back-frame::after { right: 0; width: 100px; }

  .back-title { left: 0; width: 596px; text-align: center; top: 36px; font-size: 76px; }
  .back-subtitle { left: 0; width: 592px; top: 113px; font-size: 16px; line-height: 23px; letter-spacing: 0.08em; font-weight: 400; }

  .back-blurb {
    position: absolute;
    left: 72px; top: 213px; width: 452px;
    font-family: "Poppins", sans-serif;
    font-weight: 300;
    font-size: 12.4px;
    line-height: 15.7px;
    letter-spacing: 0.06em;
    color: var(--text-soft);
    text-align: center;
  }
  .back-blurb p { margin: 0 0 15.7px; }

  .dish-photo {
    position: absolute;
    width: 192px; height: 192px;
    border-radius: 50%;
    border: 2px solid #cfcfcf;
    box-shadow: 0 0 0 3px #1a0a08, 0 0 0 4px #bdbdbd;
  }
  .dish-photo--cream { left: 95px; top: 526px; background: radial-gradient(circle at 55% 60%, #efe2b8 0%, #d9d6d2 40%, #a9a7a6 100%); }
  .dish-photo--fusilli { left: 312px; top: 526px; background: radial-gradient(circle at 50% 50%, #b8743a 0%, #c96a3a 30%, #f2f1ee 62%, #dcdcdc 100%); }

  .code-box { position: absolute; left: 325px; top: 754px; width: 229px; height: 138px; background: var(--code-box); }

  /* Spine */
  .spine-title {
    position: absolute;
    left: 600px; top: 466px;
    transform: translate(-50%, -50%) rotate(-90deg);
    font-family: "Poppins", sans-serif;
    font-size: 15.4px;
    letter-spacing: 0.09em;
    color: var(--text);
    white-space: nowrap;
    margin: 0;
  }

  /* Front cover */
  .front-title { left: 700px; width: 410px; text-align: center; top: 62px; font-size: 118px; }
  .front-subtitle { left: 690px; width: 424px; top: 196px; font-size: 23px; line-height: 35px; letter-spacing: 0.1em; font-weight: 300; }

  .front-tagline {
    position: absolute;
    right: 84px; top: 342px;
    margin: 0;
    font-family: "EB Garamond", serif;
    font-style: italic;
    font-size: 24.5px;
    line-height: 32px;
    color: var(--gold);
    text-align: right;
    white-space: nowrap;
  }
  .front-tagline .accent { color: var(--text); }
  .front-tagline .accent-number { color: var(--text); font-size: 38px; line-height: 30px; }

  .food-photo {
    position: absolute;
    left: 570px; top: 480px; width: 630px; height: 453px;
    background: radial-gradient(ellipse 300px 200px at 62% 52%, var(--food-light) 0%, var(--food-warm) 45%, transparent 100%);
  }

  .author-name {
    position: absolute;
    left: 700px; width: 404px; top: 880px;
    margin: 0;
    font-family: "Poppins", sans-serif;
    font-weight: 300;
    font-size: 16px;
    letter-spacing: 0.24em;
    color: var(--text);
    text-align: center;
    white-space: nowrap;
  }
</style>
</head>
<body>
<main class="cover-wrap">

  <section class="back-cover">
    <div class="back-frame"></div>
    <p class="title-script back-title">Kochbuch</p>
    <p class="subtitle-caps back-subtitle">Für Hobbyköche, Anfänger,<br>Berufstätige und Studenten</p>

    <div class="back-blurb">
      <p>Die Ernährung hat einen großen Einfluss auf unsere Gesundheit und unser Wohlbefinden. Selbst zu kochen bringt dabei viele Vorteile mit sich und kann zu einem wunderbaren Hobby werden. Im Gegensatz zu Fertigprodukten und Restaurantbesuchen können Sie zudem viel Geld sparen. Im Supermarkt finden Sie von frischem Obst und Gemüse bis hin zu verschiedensten Gewürzen alle Zutaten für die leckeren Gerichte aus unserem Kochbuch.</p>
      <p>Dank der unkomplizierten Rezepte können Sie auch ohne Vorkenntnisse sofort beginnen. Die Zubereitung der Speisen nimmt nur wenig Zeit in Anspruch, wodurch Sie das Kochen problemlos in Ihre Tagesplanung integrieren können. Des Weite&shy;ren finden Sie in unserem Kochbuch für Anfänger sowohl Vors&shy;peisen und Hauptgerichte als auch zahlreiche Nachspeisen. So haben Sie für jede Gelegenheit immer ein passendes Rezept parat und können Ihre Fertigkeiten in der Küche Schritt für Schritt entwickeln. Durchstöbern Sie jetzt unser Kochbuch für Anfänger und entdecken Sie Ihre Leidenschaft fürs Kochen.</p>
    </div>

    <div class="dish-photo dish-photo--cream" role="img" aria-label="Foto: Bandnudeln mit cremiger Soße auf weißem Teller"></div>
    <div class="dish-photo dish-photo--fusilli" role="img" aria-label="Foto: Vollkorn-Fusilli mit Tomaten, Spinat und Basilikum von oben"></div>

    <div class="code-box"></div>
  </section>

  <p class="spine-title">KOCHBUCH FÜR HOBBYKÖCHE, ANFÄNGER, BERUFSTÄTIGE UND STUDENTEN</p>

  <section class="front-cover">
    <div class="food-photo" role="img" aria-label="Foto: Spaghetti mit Kirschtomaten auf verziertem Teller, Mörser mit Muskatnüssen, verstreute Gewürze und Holzkochlöffel von oben"></div>

    <h1 class="title-script front-title">Kochbuch</h1>
    <h2 class="subtitle-caps front-subtitle">Für Hobbyköche, Anfänger,<br>Berufstätige und Studenten</h2>

    <p class="front-tagline">
      Mit den <span class="accent-number">150</span><br>
      besten und originellsten <span class="accent">Rezepten</span><br>
      für einen perfekten <span class="accent">Einstieg</span>
    </p>

    <p class="author-name">MATTHIAS WENDRAUER</p>
  </section>

</main>
</body>
</html>
```